Delta Ridge Arms

Firearms Website

Requirements
Must have
• we are looking for two or three pages for a new company we are starting. The Name is Delta Ridge Arms. The site will be DeltaRidgeArms.example (nothing on site at this time) We will be selling mainly handguns and products for self defense. We want this site to focus on the handgun and ammo sells as well as low cost transfers. we will handle the ecommerce part) We want a

1.) main page, mainly general information on the company.

2.) a page for sells. we will be adding the guns by hand as we place them for sell and use our credit card process. We just need the layout to fill in the items for sale on this page.

3.) navigation will be.. HOME - SALES (((guns and gun Accessories)) and self defense products) - Contact US- Transfers

company info

Delta Ridge Arms

DeltaRidgeArms.example

sales@DeltaRidgeArms.example

855-Bolt 2 Save (855-265-2728) same number for fax

412 south Walnut street

Kosciusko, ms. 39090

```html
<!DOCTYPE html>
<html lang="en">
<head>
<meta charset="utf-8">
<title>Delta Ridge Arms</title>
<link href="https://fonts.googleapis.com/css2?family=Roboto:wght@400;700;900&family=Lato:wght@400;700&family=Rubik+Dirt&family=Fjalla+One&display=swap" rel="stylesheet">
<style>
:root{
  --bg:#050507;
  --bg-purple:#1a1024;
  --header-top:#2a2a2c;
  --header-bottom:#0b0b0c;
  --orange:#f26522;
  --orange-light:#f9a11b;
  --yellow:#f7a823;
  --red:#e2231a;
  --white:#ffffff;
  --muted:#8a8a8a;
  --light:#cfcfcf;
  --card:#2a1a16;
  --stone:#3a3a3a;
  --sidebar-text:#7a7a7a;
  --sidebar-head:#c0430f;
  --green:#19a574;
  --input:#5d5b59;
}
*{margin:0;padding:0;box-sizing:border-box}
html,body{width:1036px;height:1200px;overflow:hidden}
body{
  position:relative;
  background:radial-gradient(ellipse at 50% 40%, var(--bg-purple) 0%, var(--bg) 60%);
  font-family:"Lato",sans-serif;color:var(--white);
}
.abs{position:absolute}

/* header */
.site-header{left:0;top:0;width:1036px;height:79px;background:linear-gradient(var(--header-top),var(--header-bottom));border-bottom:1px solid #222}
.brand{left:212px;top:20px;display:flex;align-items:center;gap:8px;font-family:"Roboto",sans-serif;font-weight:900;font-size:24px;color:var(--orange)}
.brand-dot{width:20px;height:20px;border-radius:50%;background:var(--orange)}
.account-links{left:651px;top:6px;font-family:"Roboto",sans-serif;font-size:7.5px;line-height:12px;color:#ddd;list-style:none}
.cart-box{left:707px;top:6px;width:122px;height:36px;background:#1d1d1e;border:1px solid #333;border-radius:3px}
.cart-title{position:absolute;left:8px;top:4px;display:flex;align-items:center;gap:6px;font-family:"Roboto",sans-serif;font-size:11px;color:#eee}
.cart-meta{position:absolute;left:6px;top:24px;font-size:7.5px;color:#ccc}
.checkout{position:absolute;right:6px;top:23px;background:var(--green);color:#fff;font-size:6px;font-weight:700;padding:1px 5px;border-radius:2px}
.main-nav{left:391px;top:53px;display:flex;gap:26px;font-family:"Roboto",sans-serif;font-weight:700;font-size:14px;list-style:none}
.main-nav li{color:#fff}
.main-nav li.active{color:var(--orange)}
.search{left:704px;top:54px;display:flex}
.search-field{width:105px;height:15px;background:#fff;color:#333;font-size:7px;padding:3px 4px;font-family:"Roboto",sans-serif}
.search-go{width:20px;height:15px;background:var(--orange);color:#fff;font-size:7.5px;font-weight:700;text-align:center;line-height:15px}

/* hero */
.hero{left:160px;top:83px;width:720px;height:347px;background:radial-gradient(ellipse at 50% 30%,#a6451a 0%,#3b1a10 35%,#141012 70%,#0a0a0c 100%)}
.hero-banner{left:330px;top:348px;width:318px;height:62px;background:#1e0f0c;transform:skewY(-4deg);display:flex;align-items:center;justify-content:center;font-family:"Rubik Dirt",sans-serif;font-size:30px;color:#f4ede4;letter-spacing:1px}
.stone-band{left:160px;width:720px;height:18px;background:linear-gradient(90deg,transparent,var(--stone) 10%,#4a4a4a 50%,var(--stone) 90%,transparent)}

/* sidebar */
.sidebar{left:210px;top:470px;width:127px;height:413px;background:#fff}
.sidebar-tab{left:210px;top:462px;width:127px;height:32px;background:linear-gradient(#f58a3a,var(--orange) 60%,#c8420f);clip-path:polygon(0 30%,18% 18%,30% 0,70% 0,82% 18%,100% 30%,100% 100%,0 100%);display:flex;align-items:center;justify-content:center;padding-top:4px;font-family:"Fjalla One",sans-serif;font-size:14px;color:#fff}
.cat-group{position:absolute;left:15px;width:105px;list-style:none}
.cat-head{font-family:"Roboto",sans-serif;font-weight:700;font-size:8.5px;color:var(--sidebar-head);height:16px;line-height:16px}
.cat-item{font-size:9px;color:var(--sidebar-text);height:17.6px;line-height:17px;border-bottom:1px solid #eee;display:flex;align-items:center;gap:5px}
.cat-item::before{content:"";width:4px;height:4px;border:1px solid #aaa}

/* products */
.section-title{left:366px;font-family:"Fjalla One",sans-serif;font-size:18px;color:#eee;letter-spacing:.3px}
.title-rule{left:366px;width:255px;height:3px;background:linear-gradient(90deg,var(--orange),transparent)}
.pager{left:804px;display:flex;gap:4px}
.card{width:144px;height:182px;background:var(--card)}
.card-photo{position:absolute;left:6px;top:6px;width:132px;height:142px;background:radial-gradient(circle at 50% 50%,#9a9a9a 0%,#d7d7d7 35%,#fff 60%)}
.card-name{position:absolute;left:7px;top:152px;font-family:"Roboto",sans-serif;font-size:8.5px;color:#fff}
.price{position:absolute;left:6px;top:168px;width:55px;height:13px;background:var(--red);clip-path:polygon(6% 0,100% 0,100% 100%,6% 100%,0 50%);font-family:"Roboto",sans-serif;font-size:8.5px;text-align:center;line-height:13px}
.add-cart{position:absolute;left:61px;top:168px;width:77px;height:13px;background:#3a3a3a;font-family:"Roboto",sans-serif;font-size:7.5px;line-height:13px;padding-left:4px;display:flex;align-items:center;gap:5px}
.sale-tag{position:absolute;left:4px;top:10px;background:var(--red);color:#fff;font-family:"Roboto",sans-serif;font-size:6.5px;font-weight:700;padding:2px 5px;transform:rotate(-30deg)}

/* footer */
.footer-title{top:994px;font-family:"Roboto",sans-serif;font-weight:700;font-size:14px;color:var(--yellow)}
.footer-title span{color:#fff}
.newsletter-text{left:210px;top:1019px;width:200px;font-size:9px;line-height:12px;color:#ddd}
.field{left:210px;width:189px;height:22px;background:var(--input);font-size:9.5px;color:#eee;padding:5px 7px}
.subscribe{left:210px;top:1125px;width:94px;height:23px;background:linear-gradient(var(--orange-light),#d35400);font-family:"Roboto",sans-serif;font-weight:700;font-size:9px;text-align:center;line-height:23px;border-radius:2px}
.services{left:443px;top:1019px;list-style:none;font-size:9px;color:#bbb;line-height:17.6px}
.about-text{left:552px;top:1019px;width:280px;font-size:9px;line-height:15.6px;color:#777}
.read-more{left:552px;top:1124px;font-size:9px;color:#fff;display:flex;align-items:center;gap:4px}
.bottom-bar{left:202px;top:1164px;width:678px;height:19px;background:#1c1c1c;font-size:8.5px;color:#ccc;display:flex;justify-content:space-between;align-items:center;padding:0 8px 0 8px}
</style>
</head>
<body>

<header class="site-header abs">
  <div class="brand abs"><span class="brand-dot"></span>Delta Ridge Arms</div>
  <ul class="account-links abs"><li>REGISTER</li><li>MY ACCOUNT</li><li>LOG IN</li></ul>
  <div class="cart-box abs">
    <div class="cart-title">
      <svg width="13" height="11" viewBox="0 0 13 11"><path d="M0 1h2l2 6h7l2-5H3" fill="none" stroke="#ddd" stroke-width="1.2"/><circle cx="5" cy="9.5" r="1" fill="#ddd"/><circle cx="10" cy="9.5" r="1" fill="#ddd"/></svg>
      My Cart
    </div>
    <div class="cart-meta">0 items ($0.00)</div>
    <div class="checkout">CHECKOUT</div>
  </div>
  <ul class="main-nav abs"><li class="active">HOME</li><li>SALES</li><li>TRANSFERS</li><li>CONTACT</li></ul>
  <div class="search abs"><div class="search-field">SEARCH</div><div class="search-go">GO</div></div>
</header>

<div class="hero abs" role="img" aria-label="Promotional photo: revolver and ammunition with two armed figures on a dark orange background"></div>
<div class="hero-banner abs">GUN CUSTOMIZATION</div>
<div class="stone-band abs" style="top:430px"></div>

<aside>
  <div class="sidebar abs">
    <ul class="cat-group" style="top:38px">
      <li class="cat-head">REVOLVER ISOLATED</li>
      <li class="cat-item">Gun Silhouette</li><li class="cat-item">Revolver Isolated</li><li class="cat-item">Corvane</li>
      <li class="cat-item">Gun Silhouette</li><li class="cat-item">Revolver Isolated</li><li class="cat-item">Corvane</li>
      <li class="cat-item">Gun Silhouette</li><li class="cat-item">Revolver Isolated</li><li class="cat-item">Corvane</li>
    </ul>
    <ul class="cat-group" style="top:229px">
      <li class="cat-head">CORVANE</li>
      <li class="cat-item">Gun Silhouette</li><li class="cat-item">Revolver Isolated</li><li class="cat-item">Corvane</li>
      <li class="cat-item">Gun Silhouette</li><li class="cat-item">Revolver Isolated</li><li class="cat-item">Corvane</li>
      <li class="cat-item">Gun Silhouette</li><li class="cat-item">Revolver Isolated</li><li class="cat-item">Corvane</li>
    </ul>
  </div>
  <div class="sidebar-tab abs">Category</div>
</aside>

<main>
  <h2 class="section-title abs" style="top:464px">Guns and Gun Accessories</h2>
  <div class="title-rule abs" style="top:495px"></div>
  <div class="pager abs" style="top:472px"><svg width="18" height="10" viewBox="0 0 18 10"><path d="M5 1L1 5l4 4M13 1l4 4-4 4" fill="none" stroke="#7a3a1a" stroke-width="1.6"/></svg></div>

  <div class="card abs" style="left:366px;top:507px"><div class="card-photo" role="img" aria-label="Product photo: semi-automatic pistol with magazine"></div><div class="sale-tag">SALE</div><div class="card-name">Product Name</div><div class="price">$890.73</div><div class="add-cart">ADD TO CART <svg width="10" height="8" viewBox="0 0 13 11"><path d="M0 1h2l2 6h7l2-5H3" fill="none" stroke="#ddd" stroke-width="1.4"/></svg></div></div>
  <div class="card abs" style="left:526px;top:507px"><div class="card-photo" role="img" aria-label="Product photo: pistol with magazine and cartridges"></div><div class="card-name">Product Name</div><div class="price">$890.73</div><div class="add-cart">ADD TO CART <svg width="10" height="8" viewBox="0 0 13 11"><path d="M0 1h2l2 6h7l2-5H3" fill="none" stroke="#ddd" stroke-width="1.4"/></svg></div></div>
  <div class="card abs" style="left:686px;top:507px"><div class="card-photo" role="img" aria-label="Product photo: compact pistol with bullets"></div><div class="card-name">Product Name</div><div class="price">$890.73</div><div class="add-cart">ADD TO CART <svg width="10" height="8" viewBox="0 0 13 11"><path d="M0 1h2l2 6h7l2-5H3" fill="none" stroke="#ddd" stroke-width="1.4"/></svg></div></div>

  <h2 class="section-title abs" style="top:705px">Defense Products</h2>
  <div class="title-rule abs" style="top:735px"></div>
  <div class="pager abs" style="top:713px"><svg width="18" height="10" viewBox="0 0 18 10"><path d="M5 1L1 5l4 4M13 1l4 4-4 4" fill="none" stroke="#7a3a1a" stroke-width="1.6"/></svg></div>

  <div class="card abs" style="left:366px;top:748px"><div class="card-photo" role="img" aria-label="Product photo: pink-framed pistol"></div><div class="card-name">Product Name</div><div class="price">$890.73</div><div class="add-cart">ADD TO CART <svg width="10" height="8" viewBox="0 0 13 11"><path d="M0 1h2l2 6h7l2-5H3" fill="none" stroke="#ddd" stroke-width="1.4"/></svg></div></div>
  <div class="card abs" style="left:526px;top:748px"><div class="card-photo" role="img" aria-label="Product photo: black pistol"></div><div class="card-name">Product Name</div><div class="price">$890.73</div><div class="add-cart">ADD TO CART <svg width="10" height="8" viewBox="0 0 13 11"><path d="M0 1h2l2 6h7l2-5H3" fill="none" stroke="#ddd" stroke-width="1.4"/></svg></div></div>
  <div class="card abs" style="left:686px;top:748px"><div class="card-photo" role="img" aria-label="Product photo: silver pistol"></div><div class="card-name">Product Name</div><div class="price">$890.73</div><div class="add-cart">ADD TO CART <svg width="10" height="8" viewBox="0 0 13 11"><path d="M0 1h2l2 6h7l2-5H3" fill="none" stroke="#ddd" stroke-width="1.4"/></svg></div></div>
</main>

<div class="stone-band abs" style="top:952px"></div>

<footer>
  <h3 class="footer-title abs" style="left:210px">NEWSLETTER</h3>
  <p class="newsletter-text abs">Not on Chirper or Facepage? No problem. Receive our coupons and special deals and a killer newsletter.</p>
  <div class="field abs" style="top:1061px">Your name:</div>
  <div class="field abs" style="top:1093px">Email address:</div>
  <div class="subscribe abs">SUBSCRIBE NOW</div>

  <h3 class="footer-title abs" style="left:443px">SERVICES</h3>
  <ul class="services abs"><li>Contact Us</li><li>About us</li><li>Help</li><li>Size Chart</li><li>Care Instructions</li><li>Shipping</li><li>Security</li></ul>

  <h3 class="footer-title abs" style="left:552px">ABOUT <span>DELTA RIDGE ARMS</span></h3>
  <p class="about-text abs">Lorem Ipsum is simply dummy text of the printing and type-setting industry. Lorem Ipsum has been the industry's standard dummy text ever since the 1500s, when an unknown printer took a galley of type and scrambled it to make a type specimen book. It has survived not only five centuries, but also the leap into electronic typesetting,</p>
  <div class="read-more abs">Read More <svg width="6" height="6" viewBox="0 0 6 6"><path d="M0 0l6 3-6 3z" fill="var(--red)"/></svg></div>

  <div class="bottom-bar abs"><span>Terms and Conditions &nbsp;|&nbsp; Privacy Policy &nbsp;|&nbsp; Sitemap</span><span>Copyright © 2013 Ridgeline LTD. All rights reserved.</span></div>
</footer>

</body>
</html>
```